Innovative healthcare collaborative needs new look for business cards

CareLoomQ is a new kind of healthcare relationship company focused on aligning partners, innovation and solutions to provide needed health services to healthcare systems, hospitals or private business. Not mired in the old merger and acquisition fee-for-service framework, we focus on primary, secondary and tertiary service area partnership collaboratives. These networks are constructed by aligning healthcare services along a network of care, not just an individual patient care plan. This involves partnership arrangements with large or small medical centers, physician groups, allied health services, public health agencies, health insurers, et al as well as civic agencies, schools, farmers, supply chains to bring about needed healthcare solutions for patients. Think Green Havens. GH does for communities what we do for hospitals and health systems. We educate and instruct on strategic, operational, and innovative solutions for a healthcare provider, practice, business, or system resulting in successful construction of care networks (legal entity). We provide the blueprint of how to do this type of partnership, focused on what’s best for the sustainability of the business and the people (patients or potential patients) living there. Rural hospitals in particular are at risk.
We also provide seminars to academic, medical academic, and private industry to instruct on how to construct these care networks and educate on the essential criteria to be successful in the new healthcare era. We have been doing this work for the past 8 years, and since COVID-19, the recognition of fractured processes has boosted the demand. We need a business card that sets the tone that the traditional healthcare delivery system in the US has transformed (overnight). Our company is educating on how to transition current business models to the new world order in this space.
Brainstormed some business card tag lines for consideration:
CareLoomQ
• a healthcaring company
• allbettertogether
• WEAVING CARE ACROSS EVERY TOWN

Target Market(s)

Health systems, hospitals, physician practices, academic medical schools, residency programs

Industry/Entity Type

Healthcare

Contact Information for Business Card

Doreen Vashtoll, Chief Relationship Officer
doreenvashtoll@mailpost-example.net
mobile: 415-286-9043

Font styles to use
Serif
Sans Serif

Requirements
Should not have
• Do not use word Consultant

```html
<!DOCTYPE html>
<html lang="en">
<head>
<meta charset="utf-8">
<title>CareLoomQ Business Card</title>
<link rel="stylesheet" href="https://fonts.googleapis.com/css2?family=Montserrat:wght@400;500;600;700&display=swap">
<style>
  :root {
    --backdrop: #8d8c8a;
    --card-dark: #151515;
    --card-light: #ffffff;
    --brand-blue: #2a6fc2;
    --brand-orange: #f7941d;
    --text-grey: #5a5a5a;
  }
  * { margin: 0; padding: 0; box-sizing: border-box; }
  html, body { width: 1200px; height: 913px; overflow: hidden; }
  body {
    background: var(--backdrop);
    font-family: "Montserrat", Arial, sans-serif;
    position: relative;
  }
  .card {
    position: absolute;
    width: 640px;
    height: 366px;
    border-radius: 26px;
    box-shadow: 0 10px 24px rgba(0,0,0,.35);
    overflow: hidden;
  }
  .card--front { left: 70px; top: 60px; background: var(--card-dark); }
  .card--back { left: 490px; top: 487px; background: var(--card-light); }

  .front-brand {
    position: absolute;
    right: 46px;
    bottom: 96px;
    display: flex;
    align-items: center;
    gap: 18px;
  }
  .brand-square {
    width: 34px; height: 34px;
    background: var(--brand-orange);
  }
  .front-brand .brand-name {
    font-size: 78px;
    font-weight: 500;
    color: var(--brand-blue);
    letter-spacing: -1px;
    line-height: 1;
  }
  .tagline {
    position: absolute;
    right: 48px;
    bottom: 62px;
    font-size: 15px;
    font-weight: 500;
    letter-spacing: 5px;
    color: var(--brand-blue);
  }

  .back-brand {
    position: absolute;
    right: 44px;
    top: 70px;
    font-size: 60px;
    font-weight: 500;
    color: var(--brand-blue);
    letter-spacing: -1px;
  }
  .person {
    position: absolute;
    left: 48px;
    top: 196px;
  }
  .person-name {
    font-size: 25px;
    font-weight: 700;
    letter-spacing: 1px;
    color: var(--brand-blue);
  }
  .person-name .surname { color: var(--brand-orange); }
  .person-title {
    margin-top: 2px;
    font-size: 14px;
    font-weight: 400;
    letter-spacing: 1px;
    color: var(--text-grey);
  }
  .contact-list {
    list-style: none;
    margin-top: 20px;
  }
  .contact-list li {
    display: flex;
    align-items: center;
    gap: 12px;
    font-size: 15px;
    color: var(--text-grey);
    margin-bottom: 6px;
  }
  .contact-list svg { width: 16px; height: 16px; fill: var(--brand-blue); flex: none; }
</style>
</head>
<body>
  <section class="card card--front">
    <div class="front-brand">
      <span class="brand-square"></span>
      <span class="brand-name">CareLoomQ</span>
    </div>
    <p class="tagline">WEAVING CARE ACROSS EVERY TOWN</p>
  </section>

  <section class="card card--back">
    <div class="back-brand">CareLoomQ</div>
    <div class="person">
      <h1 class="person-name">DOREEN <span class="surname">VASHTOLL</span></h1>
      <p class="person-title">CHIEF RELATIONSHIP OFFICER</p>
      <ul class="contact-list">
        <li>
          <svg viewBox="0 0 24 24" aria-hidden="true"><path d="M6.6 10.8a15.1 15.1 0 0 0 6.6 6.6l2.2-2.2a1 1 0 0 1 1-.25 11.4 11.4 0 0 0 3.6.57 1 1 0 0 1 1 1V20a1 1 0 0 1-1 1A17 17 0 0 1 3 4a1 1 0 0 1 1-1h3.5a1 1 0 0 1 1 1c0 1.25.2 2.45.57 3.57a1 1 0 0 1-.25 1z"/></svg>
          415-286-9043
        </li>
        <li>
          <svg viewBox="0 0 24 24" aria-hidden="true"><path d="M2 5h20v14H2z M4 7v.4l8 5.2 8-5.2V7z" fill-rule="evenodd"/></svg>
          doreenvashtoll@mailpost-example.net
        </li>
        <li>
          <svg viewBox="0 0 24 24" aria-hidden="true"><circle cx="12" cy="12" r="10"/></svg>
          www.careloomq-example.com
        </li>
      </ul>
    </div>
  </section>
</body>
</html>
```